Top of the line business card design needed for real estate brokerage

We currently have a business card with our logo but would like to have a revised version. We would love for you to implement your own design that will catch anyone's attention. The theme colors should be black, royal blue, gray/silver, and white.The contact information should be the same as the info on our current business card (picture attached). In the design that we pick, we will need to be able to edit the text so that we can customize the text content for each of our agents. Same goes for the professional picture. There should be an area on the card that each agent can have their professional portrait attached. Please include a version without the picture option as well for agents that do not wish to have a professional picture attached.

```html
<!DOCTYPE html>
<html lang="en">
<head>
<meta charset="utf-8">
<title>Clear Harbor Realty – Business Card</title>
<link href="https://fonts.googleapis.com/css2?family=PT+Sans:wght@400;700&family=Crimson+Text:wght@400;600&display=swap" rel="stylesheet">
<style>
  :root {
    --royal: #0a4ea3;
    --royal-soft: #2f6fc4;
    --ink: #1d1d1f;
    --silver: #8c8c8c;
    --silver-light: #e4e4e6;
    --paper: #ffffff;
    --backdrop: #ececec;
  }
  * { margin: 0; padding: 0; box-sizing: border-box; }
  html, body { width: 1200px; height: 1200px; overflow: hidden; }
  body {
    background: var(--backdrop);
    font-family: "PT Sans", Arial, sans-serif;
    position: relative;
  }
  .card {
    position: absolute;
    left: 198px;
    width: 803px;
    height: 520px;
    background: var(--paper);
    overflow: hidden;
  }
  .card--front { top: 64px; }
  .card--back { top: 616px; }

  .brand {
    position: absolute;
    left: 0; right: 0;
    display: flex;
    align-items: center;
    justify-content: center;
    gap: 12px;
    font-weight: 700;
    color: var(--ink);
    letter-spacing: 1px;
  }
  .brand__mark { background: var(--royal); display: block; }
  .card--front .brand { top: 150px; font-size: 34px; }
  .card--front .brand__mark { width: 22px; height: 22px; }

  .agent {
    position: absolute;
    top: 296px; left: 0; right: 0;
    text-align: center;
    font-size: 27px;
    color: var(--ink);
  }
  .agent__sep { color: var(--silver-light); margin: 0 4px; }
  .agent__role { font-family: "Crimson Text", Georgia, serif; color: var(--royal); font-size: 30px; }

  .contact-band {
    position: absolute;
    top: 359px; left: 0;
    width: 803px; height: 127px;
    background: var(--royal);
    color: var(--paper);
    font-size: 17px;
  }
  .contact-list { position: absolute; list-style: none; }
  .contact-list li { display: flex; align-items: flex-start; gap: 14px; line-height: 20px; }
  .contact-list svg { flex: none; width: 18px; height: 18px; margin-top: 1px; fill: var(--paper); }
  .contact-list b { font-weight: 700; }
  .contact-list--left { left: 96px; top: 24px; }
  .contact-list--left li + li { margin-top: 18px; }
  .contact-list--right { left: 474px; top: 24px; }
  .contact-list--right li + li { margin-top: 18px; }

  .portrait {
    position: absolute;
    left: 350px; top: 0;
    width: 103px; height: 127px;
    background: linear-gradient(180deg, #6d6d72 0%, #4b4b50 55%, #a3243b 100%);
  }

  .services {
    position: absolute;
    top: 493px; left: 0; right: 0;
    text-align: center;
    font-family: "Crimson Text", Georgia, serif;
    font-size: 16.5px;
    font-weight: 600;
    color: var(--royal);
  }

  .skyline {
    position: absolute;
    left: 60px; top: 36px;
    width: 690px; height: 380px;
    background: linear-gradient(180deg, rgba(228,228,230,0.35) 0%, rgba(214,214,218,0.7) 70%, rgba(240,240,242,0.3) 100%);
  }
  .card--back .brand { top: 212px; font-size: 56px; }
  .card--back .brand__mark { width: 34px; height: 34px; }

  .services-strip {
    position: absolute;
    top: 484px; left: 0; right: 0;
    text-align: center;
    font-size: 17px;
    font-weight: 700;
    word-spacing: 0;
  }
  .services-strip span + span { margin-left: 6px; }
  .services-strip .s-res { color: var(--royal); }
  .services-strip .s-com { color: #333; }
  .services-strip .s-pm { color: var(--royal-soft); }
  .services-strip .s-inv { color: #a5a5a5; }
</style>
</head>
<body>

<section class="card card--front">
  <div class="brand"><span class="brand__mark"></span>Clear Harbor Realty</div>

  <p class="agent">Marcus Delaine<span class="agent__sep">/</span><span class="agent__role">Broker</span></p>

  <div class="contact-band">
    <ul class="contact-list contact-list--left">
      <li>
        <svg viewBox="0 0 24 24"><path d="M6.6 10.8a15 15 0 0 0 6.6 6.6l2.2-2.2c.3-.3.7-.4 1-.2 1.1.4 2.3.6 3.6.6.6 0 1 .4 1 1V20c0 .6-.4 1-1 1A17 17 0 0 1 3 4c0-.6.4-1 1-1h3.5c.6 0 1 .4 1 1 0 1.3.2 2.5.6 3.6.1.3 0 .7-.2 1z"/></svg>
        <span>555 <b>201 4836</b> | 555 <b>201 4837</b></span>
      </li>
      <li>
        <svg viewBox="0 0 24 24"><path d="M7 3h10v4H7zM4 8h16a2 2 0 0 1 2 2v6h-4v5H6v-5H2v-6a2 2 0 0 1 2-2zm4 8v3h8v-3zm10-5a1 1 0 1 0 0 2 1 1 0 0 0 0-2z"/></svg>
        <span>555 <b>201 4899</b></span>
      </li>
    </ul>

    <div class="portrait" role="img" aria-label="Agent's professional portrait"></div>

    <ul class="contact-list contact-list--right">
      <li>
        <svg viewBox="0 0 24 24"><path d="M2 5h20v14H2zm2 2v.5l8 5.5 8-5.5V7zm0 3v7h16v-7l-8 5.5z"/></svg>
        <span>marcus@clearharborrealty.com</span>
      </li>
      <li>
        <svg viewBox="0 0 24 24"><path d="M12 2a7 7 0 0 0-7 7c0 5 7 13 7 13s7-8 7-13a7 7 0 0 0-7-7zm0 9.5A2.5 2.5 0 1 1 12 6.5a2.5 2.5 0 0 1 0 5z"/></svg>
        <span>2400 Harbor View Rd, Suite 310<br>Lakeside Cove , FL 33099</span>
      </li>
    </ul>
  </div>

  <p class="services">Residential Real Estate . Commercial Real Estate . Property Management . Investments</p>
</section>

<section class="card card--back">
  <div class="skyline" role="img" aria-label="Faint line drawing of a city skyline"></div>
  <div class="brand"><span class="brand__mark"></span>Clear Harbor Realty</div>
  <p class="services-strip">
    <span class="s-res">Residential Real Estate</span>
    <span class="s-com">Commercial Real Estate</span>
    <span class="s-pm">Property Management</span>
    <span class="s-inv">Investments</span>
  </p>
</section>

</body>
</html>
```